make our generated pages look good ( HTML ONLY)

Our application http://www.taskweave.com.au has many server side generated screens.

We wish to improve the look of these generated screens, please see attached html pages and screen shots.

Your improved look will be ported back to our screen generator so we really looking for "less is more". We really want the improved look to be based on the html pages attached so that we will be able to see the necessary changes required to our screen generator to make the same look.

We want the screens to be adaptable to different screen sizes and applicable to tablets and desktops ( maybe even phones).

**** PLEASE FOCUS ON THE CONTACT SCREEN ****
Updates

I've marked the project as "guaranteed".

**** Please note I'm expecting the attached pages to be returned looking better/more modern. See http://www.plovercode.com.au for some colors.

My goal is to be able to do a difference on the existing page and the ones that is returned so that I can make the changes to generate the pages using the better looking theme.

For the sections the fieldset/legend used for http://mrvl.taskweave.com.au/login look nice to me. Of course they need to work on all the browsers thou. 

The sections in the contact screen can be made nicer by rounding the corners.

Here are two samples :-

1. used by pixel harbour
2. used on our login page.

We use wix-dlq in our places in our application so themes/css/images from wix-dlq explorer will fit in well.

Target Market(s)

Sustainable Technology is our tag line

Requirements
Must have
• **** I WANT THE HTML PAGE BACK BUT LOOKING BETTER *****

1) Convert the attach server side generated HTML pages to be more controlled by css ( no server coding we will do that once we have a nice look)

2) We need to be able to make the same simple changes to the screen generator
Nice to have
• We would like the screens to be skinable by simply changing CSS

This is a "less is more" project, we want someone with a good eye to make these two sample pages look much nicer
Should not have
• restricted license. Any images used ( prefer no or limited images ) must be public

```html
<!DOCTYPE html>
<html lang="en">
<head>
<meta charset="utf-8">
<title>Mr Owen Tarrant: Contact</title>
<link href="https://fonts.googleapis.com/css2?family=Noto+Sans:wght@400;700&display=swap" rel="stylesheet">
<style>
:root{
  --frame:#7189ad;
  --frame-edge:#5d7699;
  --btn:#98a9c5;
  --legend:#6a86ae;
  --panel:#f2f2f2;
  --line:#d4d4d4;
  --field-line:#c9c9c9;
  --text:#333;
  --muted:#8d8d8d;
  --white:#fff;
  --marker:#f5c400;
}
*{box-sizing:border-box;margin:0;padding:0}
html,body{width:717px;height:1200px;overflow:hidden;background:var(--white)}
body{font-family:"Noto Sans",Verdana,sans-serif;font-size:9px;color:var(--text);position:relative}
.window{position:absolute;left:5px;top:5px;width:707px;height:1188px;border:1px solid var(--frame-edge);background:#e9eef5}
.title-bar{height:28px;background:var(--frame);color:var(--white);font-size:10px;padding:8px 0 0 15px}
.address-bar{position:absolute;left:9px;top:30px;width:685px;height:21px;background:var(--white);border:1px solid #c6cfdc;border-radius:3px;padding:4px 8px;font-size:9px}
.toolbar{position:absolute;left:11px;top:57px;display:flex;gap:7px}
.btn{background:var(--btn);color:var(--white);height:18px;padding:3px 0;text-align:center;font-size:9px;border-radius:2px}
.tabs{position:absolute;left:11px;top:87px;display:flex;gap:5px}
.tab{height:19px;padding:3px 10px;background:#e4e4e4;border:1px solid var(--line);border-bottom:none;border-radius:3px 3px 0 0;font-weight:700;font-size:9.5px;color:#444}
.tab.active{background:var(--white);height:20px}
.panel{position:absolute;left:11px;top:105px;width:685px;height:1078px;background:var(--panel);border:1px solid var(--line)}
.section{position:absolute;left:24px;width:626px;background:var(--white);border:1px solid var(--line);border-radius:5px}
.legend{position:absolute;left:11px;top:-10px;background:var(--legend);color:var(--white);font-weight:700;font-size:9.5px;padding:2px 9px;height:18px}
.col{position:absolute;display:flex;flex-direction:column}
.row{display:flex;align-items:center;height:19.4px}
.row label{flex:none}
.input{height:17px;border:1px solid var(--field-line);background:var(--white);color:var(--muted);padding:2px 6px;font-size:8.5px;border-radius:2px;position:relative}
.select::after{content:"";position:absolute;right:6px;top:6px;border:3px solid transparent;border-top:4px solid #444}
.textarea{height:45px}
.mini{background:var(--legend);color:var(--white);font-size:8.5px;padding:2px 8px;height:15px;border-radius:2px;margin-left:4px}
.marker{width:11px;height:9px;margin-left:4px;flex:none}
.checkbox{width:11px;height:11px;border:1px solid #c5c5c5;background:#fafafa;display:inline-block}
.categories{position:absolute;left:91px;top:68px;width:181px;height:69px;border:1px solid var(--line);padding:5px 12px}
.categories .row{gap:8px;height:20px;color:#555}
.grid{position:absolute;left:22px;top:20px;width:457px;border-collapse:collapse;font-size:8.5px}
.grid th,.grid td{border:1px solid var(--line);height:21px;padding:0 10px;text-align:left}
.grid th{font-weight:700}
.grid td.check,.grid th.check{width:40px;text-align:center;padding:0}
.editor{position:absolute;left:19px;top:24px;width:578px;height:131px;border:1px solid #c9c9c9}
.editor-tools{height:57px;background:#f0f0f0;border-bottom:1px solid #c9c9c9;display:flex;flex-direction:column;align-items:center;padding-top:3px;gap:3px}
.tool-row{display:flex;gap:4px;align-items:center;height:15px}
.tool{width:12px;height:11px;font-size:8px;font-weight:700;text-align:center;color:#222}
.tool.glyph{background:#c5ccd6;border-radius:1px;height:9px;width:10px}
.tool.faint{background:#dcdcdc}
.combo{height:14px;border:1px solid #b5b5b5;background:var(--white);font-size:8px;padding:1px 4px;position:relative}
.combo::after{content:"";position:absolute;right:3px;top:5px;border:3px solid transparent;border-top:3px solid #333}
.attach{position:absolute;left:20px;top:164px;display:flex;align-items:center;gap:8px;font-weight:700;font-size:8.5px}
</style>
</head>
<body>
<div class="window">
  <div class="title-bar">Mr Owen Tarrant:Contact - Web Viewer</div>
  <div class="address-bar">http://mrvl.taskweave.com.au</div>
  <nav class="toolbar">
    <div class="btn" style="width:48px">Ok</div>
    <div class="btn" style="width:48px">Apply</div>
    <div class="btn" style="width:48px">Delete</div>
    <div class="btn" style="width:48px">Refresh</div>
    <div class="btn" style="width:48px">Print</div>
    <div class="btn" style="width:48px">Close</div>
    <div class="btn" style="width:48px">Go Back</div>
  </nav>
  <div class="tabs">
    <div class="tab active">Quick Start</div>
    <div class="tab" style="width:53px">Misc</div>
    <div class="tab" style="width:53px">Info</div>
    <div class="tab" style="width:54px">Log</div>
  </div>

  <main class="panel">
    <!-- Contact information -->
    <section class="section" style="top:27px;height:209px">
      <div class="legend">Contact Infromation:</div>
      <div class="col" style="left:20px;top:19px">
        <div class="row"><label style="width:67px">Title:</label><div class="input select" style="width:55px">Mr</div></div>
        <div class="row"><label style="width:67px">First Name:</label><div class="input" style="width:117px">Owen</div><svg class="marker" viewBox="0 0 11 9"><ellipse cx="5" cy="4.5" rx="4.5" ry="3.8" fill="var(--marker)"/></svg></div>
        <div class="row"><label style="width:67px">Last Name:</label><div class="input" style="width:117px">Owen</div><svg class="marker" viewBox="0 0 11 9"><ellipse cx="5" cy="4.5" rx="4.5" ry="3.8" fill="var(--marker)"/></svg></div>
        <div class="row"><label style="width:67px">Business Unit:</label><div class="input" style="width:117px">Plover Code Pty Ltd</div><div class="mini">Search</div><div class="mini">View</div></div>
        <div class="row"><label style="width:67px">Work Phone:</label><div class="input" style="width:117px">8317 5092</div></div>
        <div class="row"><label style="width:67px">Mobile:</label><div class="input" style="width:117px">04130 662 248</div></div>
        <div class="row"><label style="width:67px">SMS Mobile:</label><div class="input" style="width:117px">04130 662 248</div></div>
        <div class="row"><label style="width:67px">Email:</label><div class="input" style="width:117px">owen@plovercode.com</div></div>
        <div class="row"><label style="width:67px">Fax:</label><div class="input" style="width:117px">9864 7715</div></div>
      </div>
      <div class="col" style="left:305px;top:19px">
        <div class="row"><label style="width:68px">Department:</label><div class="input" style="width:118px">IT</div></div>
        <div class="row"><label style="width:68px">Job Title:</label><div class="input" style="width:118px">System Architect</div></div>
        <div class="row"><label style="width:68px">Reports To:</label><div class="input select" style="width:74px"></div><div class="mini">View</div></div>
        <div class="row"><label style="width:68px">Home Phone:</label><div class="input" style="width:118px">9864 7715</div></div>
        <div class="row"><label style="width:68px">Web:</label><div class="input" style="width:118px">www.plovercode.com.au</div></div>
        <div class="row"><label style="width:68px">Enquiry Source:</label><div class="input select" style="width:118px"></div><div class="mini">Edit</div></div>
        <div class="row"><label style="width:68px">Account Mgr:</label><div class="input select" style="width:118px"></div><div class="mini">View</div></div>
        <div class="row"><label style="width:68px">Contact #:</label><div class="input" style="width:118px"></div></div>
      </div>
    </section>

    <!-- Address details -->
    <section class="section" style="top:255px;height:175px">
      <div class="legend">Address Details:</div>
      <div class="col" style="left:20px;top:29px">
        <div class="row" style="height:50px;align-items:flex-start"><label style="width:69px;padding-top:4px">Address:</label><div class="input textarea" style="width:146px">48 Larkhill St</div><svg class="marker" viewBox="0 0 11 9"><ellipse cx="5" cy="4.5" rx="4.5" ry="3.8" fill="var(--marker)"/></svg></div>
        <div class="row" style="height:21px"><label style="width:69px">Suburb/City</label><div class="input" style="width:144px">Kelby</div><svg class="marker" viewBox="0 0 11 9"><ellipse cx="5" cy="4.5" rx="4.5" ry="3.8" fill="var(--marker)"/></svg></div>
        <div class="row" style="height:21px"><label style="width:69px">Postcode:</label><div class="input" style="width:144px"></div><svg class="marker" viewBox="0 0 11 9"><ellipse cx="5" cy="4.5" rx="4.5" ry="3.8" fill="var(--marker)"/></svg></div>
        <div class="row" style="height:20px"><label style="width:69px">Country:</label><div class="input select" style="width:144px">Australia</div></div>
        <div class="row" style="height:20px"><label style="width:69px">State/Region:</label><div class="input select" style="width:144px">Australia</div></div>
      </div>
      <div class="col" style="left:309px;top:29px">
        <div class="row" style="height:50px;align-items:flex-start"><label style="width:68px;padding-top:4px">Address:</label><div class="input textarea" style="width:146px">48 Larkhill St</div><svg class="marker" viewBox="0 0 11 9"><ellipse cx="5" cy="4.5" rx="4.5" ry="3.8" fill="var(--marker)"/></svg></div>
        <div class="row" style="height:21px"><label style="width:68px">Suburb/City</label><div class="input" style="width:144px">Kelby</div><svg class="marker" viewBox="0 0 11 9"><ellipse cx="5" cy="4.5" rx="4.5" ry="3.8" fill="var(--marker)"/></svg></div>
        <div class="row" style="height:21px"><label style="width:68px">Postcode:</label><div class="input" style="width:144px"></div><svg class="marker" viewBox="0 0 11 9"><ellipse cx="5" cy="4.5" rx="4.5" ry="3.8" fill="var(--marker)"/></svg></div>
        <div class="row" style="height:20px"><label style="width:68px">Country:</label><div class="input select" style="width:144px">Australia</div></div>
        <div class="row" style="height:20px"><label style="width:68px">State/Region:</label><div class="input select" style="width:144px">Australia</div></div>
      </div>
    </section>

    <!-- Classification -->
    <section class="section" style="top:447px;height:175px">
      <div class="legend">Classification:</div>
      <div class="col" style="left:22px;top:24px">
        <div class="row" style="height:21px"><label style="width:69px">Position Class:</label><div class="input select" style="width:144px"></div></div>
        <div class="row" style="height:21px"><label style="width:69px">Revenue:</label><div class="input" style="width:145px"></div></div>
        <div class="row" style="height:14px"><label>Categories:</label></div>
      </div>
      <div class="categories">
        <div class="row"><span class="checkbox"></span>Name</div>
        <div class="row"><span class="checkbox"></span>Business Partner</div>
        <div class="row"><span class="checkbox"></span>Newsletter Testing</div>
      </div>
      <div class="mini" style="position:absolute;left:87px;top:142px;width:37px;text-align:center">Add</div>
      <div class="col" style="left:313px;top:24px">
        <div class="row" style="height:21px"><label style="width:68px">Industry:</label><div class="input select" style="width:144px"></div></div>
        <div class="row" style="height:21px"><label style="width:68px">Sub Industry:</label><div class="input select" style="width:144px"></div></div>
      </div>
    </section>

    <!-- Campaigns -->
    <section class="section" style="top:641px;height:117px">
      <div class="legend">Campaigns:</div>
      <table class="grid">
        <tr><th style="width:232px">Title</th><th>Result</th><th class="check"><span class="checkbox"></span></th></tr>
        <tr><td>TechFair 2005</td><td></td><td class="check"><span class="checkbox"></span></td></tr>
        <tr><td>Demo 2</td><td></td><td class="check"><span class="checkbox"></span></td></tr>
      </table>
      <div class="mini" style="position:absolute;left:19px;top:88px;width:37px;text-align:center">Add</div>
    </section>

    <!-- Marketing control -->
    <section class="section" style="top:780px;height:48px">
      <div class="legend">Marketing Control:</div>
      <div class="row" style="position:absolute;left:24px;top:19px;font-weight:700;gap:6px">No Group Emails: <span class="checkbox"></span></div>
    </section>

    <!-- Notes & attachments -->
    <section class="section" style="top:853px;height:195px">
      <div class="legend">Notes &amp; Attachments:</div>
      <div class="editor">
        <div class="editor-tools">
          <div class="tool-row">
            <span class="tool">B</span><span class="tool" style="font-style:italic">I</span><span class="tool" style="text-decoration:underline">U</span><span class="tool" style="text-decoration:line-through;font-size:6px">ABC</span>
            <span class="tool glyph"></span><span class="tool glyph"></span><span class="tool glyph"></span><span class="tool glyph"></span>
            <span class="combo" style="width:61px">Format</span><span class="combo" style="width:62px">Font family</span><span class="combo" style="width:61px">Font size</span>
          </div>
          <div class="tool-row">
            <span class="tool glyph"></span><span class="tool glyph"></span><span class="tool glyph"></span><span class="tool glyph"></span><span class="tool glyph"></span><span class="tool glyph"></span><span class="tool glyph"></span>
            <span class="tool glyph"></span><span class="tool glyph"></span><span class="tool glyph faint"></span><span class="tool glyph faint"></span>
            <span class="tool glyph faint"></span><span class="tool glyph faint"></span><span class="tool glyph"></span><span class="tool glyph"></span><span class="tool glyph"></span><span class="tool glyph"></span><span class="tool glyph"></span>
            <span class="tool glyph"></span><span class="tool glyph"></span><span class="tool" style="color:#2a4d99">A</span><span class="tool glyph"></span>
          </div>
          <div class="tool-row">
            <span class="tool glyph"></span><span class="tool glyph faint"></span><span class="tool glyph faint"></span><span class="tool glyph faint"></span><span class="tool glyph faint"></span><span class="tool glyph faint"></span>
            <span class="tool glyph faint"></span><span class="tool glyph faint"></span><span class="tool glyph faint"></span><span class="tool glyph faint"></span><span class="tool glyph faint"></span>
            <span class="tool">—</span><span class="tool glyph"></span><span class="tool glyph" style="outline:1px solid #3b66b3"></span>
            <span class="tool">x<sub>2</sub></span><span class="tool">x<sup>2</sup></span><span class="tool">Ω</span>
            <svg width="11" height="11" viewBox="0 0 11 11"><circle cx="5.5" cy="5.5" r="5" fill="var(--marker)"/></svg>
            <span class="tool glyph"></span>
          </div>
        </div>
      </div>
      <div class="attach">Attachment
        <svg width="10" height="16" viewBox="0 0 10 16"><path d="M7 4v8a2.5 2.5 0 0 1-5 0V3a1.6 1.6 0 0 1 3.2 0v8.5a.6.6 0 0 1-1.2 0V5" fill="none" stroke="#555" stroke-width="1"/></svg>
        <svg width="14" height="14" viewBox="0 0 14 14"><circle cx="8" cy="6" r="4.2" fill="none" stroke="#555" stroke-width="1.2"/><path d="M5 9L1.5 12.5" stroke="#555" stroke-width="1.6"/></svg>
      </div>
    </section>
  </main>
</div>
</body>
</html>
```